Marlowe Racquet Commons needs a brochure & leaflet/poster designed!

We need a tri-fold A5 brochure and poster/flyer designed. Both designs should follow the same scheme and be designed so each can be used for different content. Colour scheme should be based around the the green on attached logo with contrast light grey. See colour scheme of examples attached, as this is the type of thing we are looking for, but using the green colour.

Tri-fold A5 Brochure - will become our information pamphlet to showcase Marlowe Racquet Commons. Attached is the current leaflet (we do not need a full page with online booking instructions though). We want a more fresh and modern look with a better front page. Need to include sections for a welcome introduction, how to book a court (simplified and shorter), Coaching (larger section for coaching), Cafe, Marlowe Lawn Society and Local Tennis Leagues. It needs to be generic so we can in future update content when needed. I have also added a few brochures that we have found online, to give you a feel of the type of design we're looking for.

Poster/leaflet - a generic leaflet/poster that can be updated with current offers and info. Should include pictures, area for key message and contact details section at bottom. Include social media icons (FB, Twitter). Should follow the same scheme as all other material. Should be able to print in either A5/A4/A3

I have attached some pictures to use and the logo too.
Updates

Target Market(s)

Tennis, sports

Industry/Entity Type

Community

Font styles to use
Serif

Colors
00a990
aaaaaa
5c5c5c

Requirements
Must have
• Similar structure to the attached examples, giving you a feeling of the look and feel we are after!
Should not have
• Should not look like current brochure, need a full re-design

```html
<!DOCTYPE html>
<html lang="en">
<head>
<meta charset="utf-8">
<title>Things 2 Do – Marlowe Racquet Commons</title>
<link href="https://fonts.googleapis.com/css2?family=Open+Sans:ital,wght@0,300;0,400;0,600;0,700;1,700;1,800&display=swap" rel="stylesheet">
<style>
  :root {
    --teal: #00a990;
    --lime: #c9d92c;
    --ink: #1d3524;
    --grey: #aaaaaa;
    --charcoal: #5c5c5c;
    --white: #ffffff;
  }
  html, body { margin: 0; padding: 0; overflow: hidden; }
  body { width: 799px; height: 1200px; background: var(--white); font-family: "Open Sans", sans-serif; }
  .poster { position: relative; width: 799px; height: 1200px; overflow: hidden; background: var(--white); }
  .hero-photo {
    position: absolute; left: 0; top: 0; width: 799px; height: 640px;
    background: linear-gradient(160deg, #8fae9c 0%, #6f8f95 35%, #3f6f8a 60%, #b9a48f 100%);
  }
  .shapes { position: absolute; left: 0; top: 0; width: 799px; height: 1200px; }
  .title {
    position: absolute; right: 22px; top: 112px; margin: 0;
    font-weight: 300; font-size: 60px; letter-spacing: 1px; color: var(--white);
  }
  .tagline-band {
    position: absolute; left: 378px; top: 328px; width: 421px; height: 60px;
    background: rgba(120, 130, 130, 0.55);
  }
  .tagline {
    position: absolute; right: 22px; top: 332px; margin: 0;
    font-weight: 300; font-size: 34px; color: var(--white);
  }
  .offer {
    position: absolute; left: 40px; top: 620px; width: 640px;
    transform: rotate(-12.7deg); transform-origin: left top; color: var(--ink);
  }
  .offer h2 { margin: 0; font-style: italic; font-weight: 700; line-height: 1.05; }
  .offer .line-one { font-size: 34px; }
  .offer .line-two { font-size: 40px; font-weight: 800; margin-bottom: 10px; }
  .offer p { margin: 0; font-size: 17px; line-height: 29px; width: 630px; }
  .offer strong { font-weight: 700; }
  .contact { position: absolute; left: 118px; top: 1046px; }
  .phone { margin: 0 0 22px; font-weight: 300; font-size: 40px; color: var(--teal); letter-spacing: 1px; line-height: 1.1; }
  .contact ul { list-style: none; margin: 0; padding: 0; font-size: 14.5px; font-weight: 700; color: var(--ink); line-height: 1.75; }
  .contact li::before { content: "•"; margin-right: 6px; }
  .brand { position: absolute; left: 450px; top: 910px; width: 330px; text-align: center; }
  .brand-dot { width: 120px; height: 120px; border-radius: 50%; background: var(--lime); margin: 0 auto 98px 30px; }
  .brand-name { margin: 0; font-size: 19px; font-weight: 400; color: var(--teal); letter-spacing: 0.5px; text-transform: uppercase; }
</style>
</head>
<body>
<main class="poster">
  <div class="hero-photo" role="img" aria-label="Photo of smiling children peeking through a tennis racquet's strings"></div>

  <svg class="shapes" viewBox="0 0 799 1200" aria-hidden="true">
    <polygon points="0,450 140,540 0,610" fill="var(--teal)"/>
    <polygon points="0,585 799,405 799,830 0,1000" fill="var(--lime)"/>
    <polygon points="0,1035 0,1200 92,1200" fill="var(--lime)"/>
    <polygon points="92,1200 0,1035 0,1010 110,1200" fill="var(--teal)"/>
  </svg>

  <h1 class="title">THINGS 2 DO</h1>
  <div class="tagline-band"></div>
  <p class="tagline">Book, Play &amp; Enjoy</p>

  <section class="offer">
    <h2 class="line-one">Coaching: Tennis Club:</h2>
    <h2 class="line-two">Local League: Pavilion Cafe</h2>
    <p>Now that you have your key fob you may fancy getting some tips from our coaching team for you or your fellow householders. the team are run by local county coaches owen hartley and gareth pell who have over 30 years experience teaching all ages and abilities. you can contact the coaching team directly on <strong>info@marlowecoachingacademy.org.uk</strong> to discuss your requirements. the team aim to put on session that cater for everybody's needs so if you have idea for session you would like please contact the team and they would be happy to help.</p>
  </section>

  <section class="contact">
    <p class="phone">01632 960495</p>
    <ul>
      <li>info@marloweracquetcommons.org.uk</li>
      <li>www.marloweracquetcommons.org.uk</li>
    </ul>
  </section>

  <div class="brand">
    <div class="brand-dot"></div>
    <p class="brand-name">Marlowe Racquet Commons</p>
  </div>
</main>
</body>
</html>
```